My colors are BLACK, WHITE AND RED. I want something super professional but feminine and a bit sassy. My original logo is gold and black, I would like to see the crown in red (still with gradient) . I have a suggested layout in the files but am totally open to fresh ideas. I'm torn about having a little crown on the front as well as large logo on the back.

Target Market(s)

People buying high end houses

Font styles to use
Serif
Sans Serif

Requirements
Must have
• all the verbiage and text needed is on the business card in the files.
Nice to have
• classy, pretty, elegant, business like
Should not have
• cheesy, guady, boring

```html
<!DOCTYPE html>
<html lang="en">
<head>
<meta charset="utf-8">
<title>Marion Delacroix – Business Card</title>
<link rel="stylesheet" href="https://fonts.googleapis.com/css2?family=Cinzel:wght@400;600&family=Montserrat:wght@400;500&family=Tinos:ital@0;1&display=swap">
<style>
  :root {
    --canvas: #d9d9d9;
    --ink: #111111;
    --card-black: #050505;
    --white: #ffffff;
    --red: #e0262b;
    --orange: #f39a1e;
    --gold: #f2b833;
    --soft-grey: #d6d6d6;
    --photo-dark: #1a1a1a;
    --photo-mid: #6e4a36;
  }
  * { margin: 0; padding: 0; box-sizing: border-box; }
  html, body { width: 900px; height: 1200px; overflow: hidden; background: var(--canvas); }
  .stage { position: relative; width: 900px; height: 1200px; }

  .card {
    position: absolute; left: 82px; width: 733px; height: 430px;
    border-radius: 28px; overflow: hidden;
  }
  .card--front { top: 137px; background: var(--white); }
  .card--back { top: 633px; background: var(--card-black); color: var(--white); text-align: center; }

  .front-art { position: absolute; inset: 0; }
  .centered { position: absolute; left: 368px; width: 340px; text-align: center; }

  .brand-mark {
    top: 84px; font-family: "Cinzel", serif; font-weight: 600;
    font-size: 22px; letter-spacing: 3px; color: var(--red);
  }
  .agent-name {
    top: 146px; font-family: "Cinzel", serif; font-weight: 600;
    font-size: 31px; color: var(--ink); white-space: nowrap;
  }
  .agent-title {
    top: 188px; font-family: "Montserrat", sans-serif; font-size: 20px;
    letter-spacing: 1px; color: var(--red);
  }
  .credentials {
    top: 221px; list-style: none; font-family: "Tinos", serif;
    font-size: 16.5px; line-height: 26px; color: var(--ink);
  }
  .contact-row {
    position: absolute; left: 374px; top: 350px; display: flex; align-items: center;
  }
  .agency-name {
    font-family: "Montserrat", sans-serif; font-weight: 500; font-size: 14px;
    line-height: 18px; color: var(--red); width: 118px;
  }
  .contact-divider { width: 1px; height: 42px; background: #888; margin: 0 10px 0 8px; }
  .contact-details {
    font-family: "Montserrat", sans-serif; font-size: 16px; line-height: 21px;
    color: var(--ink); white-space: nowrap;
  }

  .back-mark {
    position: absolute; left: 0; right: 0; top: 84px;
    font-family: "Cinzel", serif; font-weight: 600; font-size: 30px;
    letter-spacing: 4px; color: var(--red);
  }
  .back-first {
    position: absolute; left: 0; right: 0; top: 164px;
    display: flex; justify-content: center; align-items: center; gap: 10px;
    font-family: "Cinzel", serif; font-size: 27px; color: var(--gold); letter-spacing: 1px;
  }
  .back-first::before, .back-first::after {
    content: ""; width: 78px; height: 2px; background: var(--gold);
  }
  .back-last {
    position: absolute; left: 0; right: 0; top: 194px;
    font-family: "Cinzel", serif; font-size: 37px; letter-spacing: 16px; padding-left: 16px;
  }
  .dash { position: absolute; left: 357px; width: 18px; height: 2px; background: var(--red); }
  .award {
    position: absolute; left: 0; right: 0; top: 257px;
    font-family: "Cinzel", serif; font-size: 18.5px; color: var(--soft-grey);
  }
  .tagline {
    position: absolute; left: 0; right: 0; font-family: "Tinos", serif;
    font-style: italic; font-size: 16.5px; color: var(--red);
  }
  .office {
    position: absolute; left: 0; right: 0; top: 326px;
    font-family: "Montserrat", sans-serif; font-size: 14.5px;
  }
  .housing-badge {
    position: absolute; left: 40px; top: 356px; width: 48px; height: 48px;
    background: var(--red); border-radius: 4px;
  }
</style>
</head>
<body>
<main class="stage">

  <section class="card card--front">
    <svg class="front-art" width="733" height="430" viewBox="0 0 733 430">
      <defs>
        <linearGradient id="arcGlow" x1="0" y1="0" x2="0" y2="1">
          <stop offset="0" stop-color="var(--red)"/>
          <stop offset="0.5" stop-color="var(--gold)"/>
          <stop offset="1" stop-color="var(--red)"/>
        </linearGradient>
        <linearGradient id="portraitTone" x1="0" y1="0" x2="0" y2="1">
          <stop offset="0" stop-color="var(--photo-mid)"/>
          <stop offset="0.35" stop-color="var(--photo-dark)"/>
          <stop offset="1" stop-color="var(--photo-dark)"/>
        </linearGradient>
      </defs>
      <path d="M0 0 H250 Q375 215 250 430 H0 Z" fill="var(--card-black)"/>
      <path d="M250 0 Q375 215 250 430" fill="none" stroke="url(#arcGlow)" stroke-width="6"/>
      <path d="M266 0 Q395 215 270 430" fill="none" stroke="url(#arcGlow)" stroke-width="3" opacity="0.8"/>
      <rect x="8" y="20" width="230" height="410" rx="40" fill="url(#portraitTone)"
            role="img" aria-label="Portrait photo of the agent in a dark blazer and white blouse"/>
    </svg>

    <div class="centered brand-mark">Delacroix Group</div>
    <h1 class="centered agent-name">Marion Delacroix</h1>
    <p class="centered agent-title">REAL ESTATE AGENT</p>
    <ul class="centered credentials">
      <li>Certified Mountain Area Specialist</li>
      <li>Certified Luxury Home Marketing Specialist</li>
      <li>Certified Negotiation Expert</li>
    </ul>
    <div class="contact-row">
      <div class="agency-name">Summit Realty Group</div>
      <div class="contact-divider"></div>
      <div class="contact-details">
        <div>720-555-0183</div>
        <div>mdelacroix@summit.net</div>
      </div>
    </div>
  </section>

  <section class="card card--back">
    <div class="back-mark">Delacroix Group</div>
    <div class="back-first">MARION</div>
    <div class="back-last">DELACROIX</div>
    <span class="dash" style="top:246px"></span>
    <div class="award">PLATINUM CLUB AWARD 2018</div>
    <div class="tagline" style="top:284px">Top Producing Individual Agent Evergreen office 2018</div>
    <span class="dash" style="top:314px"></span>
    <div class="office">1200 Ridgeline Rd. Evergreen, Co 80439 | Office : 303-555-0126</div>
    <div class="tagline" style="top:349px">Each office indipendently owned and operated</div>
    <div class="housing-badge" role="img" aria-label="Fair housing badge"></div>
  </section>

</main>
</body>
</html>
```